Natural Immune System Booster

We need a pharmaceutical type box and label design for a vitamin supplement product. Korvelix is in process of being trademarked and should therefore carry the TM symbol. It is comprised of a special blend of over 20 vitamins, herbs and minerals with a High strength vitamin C booster. The tag line should read. The No.1 Natural Support For Your Immune System. Each tube contains 10 tablets. A bar code will be placed on the box carton. We prefer bright and vivid colours, preferably a mix of electric purple, yellow and orange mix. We have three flavours, summer berry (strawberry), tropical fruit and juicy orange - the box and label should indicate the flavours in a creative design element. Effervescent tabelts should be clearly marked on the box and label. The ingredients and instructions should be present on the box outer carton and also the label. We require an eye catching yet simple and bright design that pops off the shelf.
Updates

Target Market(s)

Target customers are male and female 20 - 60+ that live in Western countries that handle household budgets.

Industry/Entity Type

Pharmaceutical

Requirements
Must have
• Please see current box design, all necessary elements and specifications are included here. We require same to be placed on new design.

I have attached a txt file of the supplement facts and other details that are required for both the label and the box

```html
<!DOCTYPE html>
<html lang="en">
<head>
<meta charset="utf-8">
<title>Korvelix Vitamin Supplement – Flavour Labels</title>
<link href="https://fonts.googleapis.com/css2?family=Lato:wght@300;400;700&display=swap" rel="stylesheet">
<style>
  :root {
    --ink: #1a1a1a;
    --white: #ffffff;
    --header-shade: #e6e6e6;
    --berry-top: #9a5bb4;
    --berry-bottom: #6a2a8c;
    --berry-text: #7b3199;
    --berry-fruit-a: #c0394f;
    --berry-fruit-b: #2a1b3a;
    --orange-top: #f7921e;
    --orange-bottom: #ffe500;
    --orange-accent: #1d8d3e;
    --orange-text: #1f5a1f;
    --orange-fruit-a: #ffb23a;
    --orange-fruit-b: #f07a10;
  }
  * { margin: 0; padding: 0; box-sizing: border-box; }
  html, body { width: 960px; height: 1200px; overflow: hidden; background: var(--white); }
  body { position: relative; font-family: "Lato", sans-serif; color: var(--ink); }

  .label { position: absolute; top: 50px; width: 420px; height: 1123px; }
  .label--berry { left: 29px; --accent: var(--berry-text); }
  .label--orange { left: 517px; --accent: var(--orange-accent); }
  .label__bg { position: absolute; inset: 0; width: 100%; height: 100%; }

  .brand { position: absolute; top: 22px; left: 0; width: 100%; text-align: center; }
  .brand__name { font-size: 64px; font-weight: 400; line-height: 1; color: var(--ink); letter-spacing: 1px; }
  .brand__type { font-size: 29px; font-weight: 300; line-height: 1; margin-top: 6px; letter-spacing: 0.5px; }

  .tagline { position: absolute; top: 178px; left: 0; width: 100%; text-align: center; }
  .tagline__lead { font-size: 60px; font-weight: 300; line-height: 1.05; }
  .tagline__lead b { font-weight: 700; color: var(--accent); }
  .tagline__line { font-size: 34px; font-weight: 300; line-height: 1.05; }
  .tagline__strong { font-size: 33px; font-weight: 700; line-height: 1.15; color: var(--accent); }

  .fruit { position: absolute; left: 45px; top: 505px; width: 330px; height: 235px; border-radius: 50%; }
  .label--berry .fruit { background: radial-gradient(ellipse at 40% 55%, var(--berry-fruit-a) 0%, #7a2a5a 45%, var(--berry-fruit-b) 85%, transparent 100%); }
  .label--orange .fruit { background: radial-gradient(ellipse at 50% 55%, var(--orange-fruit-a) 0%, var(--orange-fruit-b) 60%, transparent 100%); }

  .flavour { position: absolute; top: 818px; left: 0; width: 100%; text-align: center; line-height: 1; }
  .flavour__top { font-size: 70px; font-weight: 300; letter-spacing: 2px; }
  .flavour__bottom { font-size: 88px; font-weight: 400; margin-top: 6px; }
  .label--berry .flavour { color: var(--white); }
  .label--orange .flavour { color: var(--orange-text); }
  .label--orange .flavour__bottom { font-weight: 700; }

  .count { position: absolute; bottom: 14px; left: 0; width: 100%; text-align: center; font-size: 28px; font-weight: 400; color: var(--accent); }
  .count b { font-weight: 700; }
  .label--orange .count { color: var(--orange-text); }
</style>
</head>
<body>

<section class="label label--berry">
  <svg class="label__bg" viewBox="0 0 420 1123" preserveAspectRatio="none" aria-hidden="true">
    <defs>
      <linearGradient id="berryFill" x1="0" y1="0" x2="0" y2="1">
        <stop offset="0" stop-color="#9a5bb4"/>
        <stop offset="1" stop-color="#6a2a8c"/>
      </linearGradient>
      <linearGradient id="headWhite" x1="0" y1="0" x2="0" y2="1">
        <stop offset="0" stop-color="#f4f4f4"/>
        <stop offset="0.12" stop-color="#ffffff"/>
        <stop offset="0.8" stop-color="#ffffff"/>
        <stop offset="1" stop-color="#e4e4e4"/>
      </linearGradient>
    </defs>
    <rect x="0" y="0" width="420" height="1123" fill="url(#berryFill)"/>
    <path d="M0 0 H420 V402 Q210 462 0 402 Z" fill="#5c2379" opacity="0.45"/>
    <path d="M0 0 H420 V390 Q210 450 0 390 Z" fill="url(#headWhite)"/>
    <path d="M72 1123 Q74 1046 210 1043 Q346 1046 348 1123 Z" fill="#ffffff"/>
  </svg>
  <div class="brand">
    <div class="brand__name">Korvelix™</div>
    <div class="brand__type">VITAMIN SUPPLEMENT</div>
  </div>
  <div class="tagline">
    <div class="tagline__lead">The <b>No.1</b></div>
    <div class="tagline__line">Natural Support</div>
    <div class="tagline__line">For Your</div>
    <div class="tagline__strong">Immune System</div>
  </div>
  <div class="fruit" role="img" aria-label="Photo of raspberries, blackberries and blueberries with a mint leaf"></div>
  <div class="flavour">
    <div class="flavour__top">SUMMER</div>
    <div class="flavour__bottom">BERRY</div>
  </div>
  <div class="count"><b>10</b> tablets</div>
</section>

<section class="label label--orange">
  <svg class="label__bg" viewBox="0 0 420 1123" preserveAspectRatio="none" aria-hidden="true">
    <defs>
      <linearGradient id="orangeFill" x1="0" y1="0" x2="0" y2="1">
        <stop offset="0.3" stop-color="#f7921e"/>
        <stop offset="1" stop-color="#ffe500"/>
      </linearGradient>
      <linearGradient id="headWhite2" x1="0" y1="0" x2="0" y2="1">
        <stop offset="0" stop-color="#f4f4f4"/>
        <stop offset="0.12" stop-color="#ffffff"/>
        <stop offset="0.8" stop-color="#ffffff"/>
        <stop offset="1" stop-color="#e4e4e4"/>
      </linearGradient>
    </defs>
    <rect x="0" y="0" width="420" height="1123" fill="url(#orangeFill)"/>
    <path d="M0 0 H420 V402 Q210 462 0 402 Z" fill="#e57a10" opacity="0.5"/>
    <path d="M0 0 H420 V390 Q210 450 0 390 Z" fill="url(#headWhite2)"/>
    <path d="M72 1123 Q74 1046 210 1043 Q346 1046 348 1123 Z" fill="#ffffff"/>
  </svg>
  <div class="brand">
    <div class="brand__name">Korvelix™</div>
    <div class="brand__type">VITAMIN SUPPLEMENT</div>
  </div>
  <div class="tagline">
    <div class="tagline__lead">The <b>No.1</b></div>
    <div class="tagline__line">Natural Support</div>
    <div class="tagline__line">For Your</div>
    <div class="tagline__strong">Immune System</div>
  </div>
  <div class="fruit" role="img" aria-label="Photo of whole and sliced oranges with a green leaf"></div>
  <div class="flavour">
    <div class="flavour__top">JUICY</div>
    <div class="flavour__bottom">ORANGE</div>
  </div>
  <div class="count"><b>10</b> tablets</div>
</section>

</body>
</html>
```